Redesign Company Website

Cellar Loop new website: www.cellarloop.com.au

Brief

• Cellar Loop
Cellar Loop is a relationship marketing company offering telesales services to partner wineries. We manage the winery’s database, engage in telesales campaigns and return great sales results to the winery.
Cellar Loop currently operates in Australia, New Zealand and Canada, with plans to expand to the USA in 2014.

• The service
We take the winery’s database, clean it up, and typically run 2 telesales campaigns per year. The timing, products and pricing are agreed with the winery prior to the campaign.
There are multiple benefits for the winery: the database is engaged with the winery, sales conversions are high and the database is reliable and up to date.

• The size of the company
Cellar Loop International employs about 20 people and plans to grow to 30. The turnover is in excess of AU$5m

• How long have you been established?
Cellar Loop was rebranded 12 months ago, but the original entity has been trading for 10 years.

• The company in a few words
Dynamic
Responsive
Detailed
Bright
Independent
Friendly
Engaging

The old web site

www.cellarloop.com.au

• What is good about the web site?
Clean look, succinct. No need to scroll down to get information.

• What don’t you like about the old web site?
Blocky top graphics look too cartoon-like
Stock photos
Dull, corporate look with no personality
Bad infographic on Services page
Limited contact information
Too much red

The new web site

• Outline the aims of the new web site
The main aim of the new website is to represent Cellar Loop and its personality better. We hope to be able to engage wineries to come back to the site. It has to contain the relevant service and benefit information to convert new winery business.

• Who is the target audience?
This is above all a B2B website aimed at winery partners
It is not an e-commerce site, but we want wineries to come back frequently.

• How will your target audience be accessing your site
All forms, probably including mobile phones.

• What are the unique selling points for your company, your products or your services?
Independent
Reliable
Secure

• Competitors' web sites:
www.vintrackers.com.au
http://www.morvellcasksupply.com.au/

The look and feel of the new web site

• Various web sites that we like the look & feel of.
http://www.tarbeck.com.au/ Great graphic on home page, good use of white space, uncluttered
http://pemvask.com/ Good use of space, clear navigation, bit quirky
http://www.casaorlen.com.au/ Ease of navigation, like the drop down “where we are” on the home page
http://www.starpilotnotes.co.uk/ Great use of graphics for navigation etc.

• Logo and sample of corporate identity files attached.

Wineries in Australia, NZ, Canada, USA

Nice to have
• Would be good to have a blog on the site to create new content easily and frequently

```html
<!DOCTYPE html>
<html lang="en">
<head>
<meta charset="utf-8">
<title>Cellar Loop</title>
<link rel="stylesheet" href="https://fonts.googleapis.com/css2?family=Lato:wght@300;400;700&display=swap">
<style>
  :root {
    --white: #ffffff;
    --ink: #333333;
    --accent: #e21b2c;
    --nav-band: rgba(255, 255, 255, 0.28);
    --footer-band: rgba(255, 255, 255, 0.88);
    --social-bg: rgba(255, 255, 255, 0.45);
    --divider: #999999;
  }
  * { box-sizing: border-box; margin: 0; padding: 0; }
  html, body { width: 1200px; height: 697px; overflow: hidden; }
  body { font-family: "Lato", sans-serif; color: var(--white); }

  .page { position: relative; width: 1200px; height: 697px; overflow: hidden; }

  .hero-photo {
    position: absolute; inset: 0;
    background:
      radial-gradient(ellipse at 50% 55%, rgba(40,50,75,0.55), transparent 60%),
      linear-gradient(180deg, #c79a62 0%, #a8763f 35%, #7d5a3a 65%, #4a3a36 100%);
  }

  .brand {
    position: absolute; top: 52px; left: 0; width: 1200px; text-align: center;
    font-size: 40px; font-weight: 400; line-height: 48px; color: var(--white);
    letter-spacing: 1px;
  }

  .social {
    position: absolute; top: 61px; right: 87px; display: flex; gap: 9px; list-style: none;
  }
  .social li {
    width: 35px; height: 35px; border-radius: 50%; background: var(--social-bg);
  }
  .social li:first-child { background: var(--white); }

  .main-nav {
    position: absolute; top: 142px; left: 0; width: 1200px; height: 76px;
    background: var(--nav-band);
  }
  .main-nav ul {
    list-style: none; display: flex; justify-content: center;
    height: 100%; align-items: center;
  }
  .main-nav li { margin: 0 34px; font-size: 15px; letter-spacing: 1.5px; text-transform: uppercase; }
  .main-nav li.is-current { text-decoration: underline; text-underline-offset: 5px; }

  .hero-copy {
    position: absolute; top: 368px; left: 0; width: 1200px; text-align: center;
    text-shadow: 0 1px 4px rgba(0,0,0,0.35);
  }
  .hero-title {
    font-weight: 300; font-size: 52px; line-height: 60px; text-transform: uppercase;
  }
  .hero-text {
    margin: 22px auto 0; width: 830px; font-size: 18px; line-height: 26px;
  }

  .slider-arrow { position: absolute; top: 472px; }
  .slider-arrow.prev { left: 86px; }
  .slider-arrow.next { right: 86px; }

  .site-footer {
    position: absolute; bottom: 0; left: 0; width: 1200px; height: 44px;
    background: var(--footer-band); color: var(--ink);
    display: flex; align-items: center; justify-content: space-between;
    padding: 0 87px;
  }
  .regions { list-style: none; display: flex; font-size: 15px; }
  .regions li { padding: 0 7px; border-left: 1px solid var(--divider); text-transform: uppercase; }
  .regions li:first-child { padding-left: 0; border-left: 0; }
  .contacts { display: flex; gap: 28px; font-size: 16px; font-weight: 700; }
  .contacts span { display: flex; align-items: center; gap: 8px; }
</style>
</head>
<body>
<div class="page">
  <div class="hero-photo" role="img" aria-label="Couple smiling and tasting white wine in front of oak barrels"></div>

  <header class="brand">Cellar Loop</header>

  <ul class="social" aria-label="Social links">
    <li></li><li></li><li></li><li></li>
  </ul>

  <nav class="main-nav">
    <ul>
      <li class="is-current">Home</li>
      <li>About Us</li>
      <li>Services</li>
      <li>Benefits</li>
      <li>Testimonials</li>
      <li>Contact</li>
    </ul>
  </nav>

  <section class="hero-copy">
    <h1 class="hero-title">You make great wine<br>leave the rest to us</h1>
    <p class="hero-text">Our staff are highly trained in every aspect of your products and learn the values of your brand and what it represents. When your customers are contacted by Cellar Loop, they will feel as if they had just spoken with a member of your own team.</p>
  </section>

  <svg class="slider-arrow prev" width="26" height="60" viewBox="0 0 26 60" aria-label="Previous slide"><polyline points="24,2 2,30 24,58" fill="none" stroke="#fff" stroke-width="2"/></svg>
  <svg class="slider-arrow next" width="26" height="60" viewBox="0 0 26 60" aria-label="Next slide"><polyline points="2,2 24,30 2,58" fill="none" stroke="#fff" stroke-width="2"/></svg>

  <footer class="site-footer">
    <ul class="regions">
      <li>Australia</li><li>New Zeeland</li><li>Hong Kong</li><li>Canada</li>
    </ul>
    <div class="contacts">
      <span>
        <svg width="20" height="20" viewBox="0 0 24 24" aria-hidden="true"><path fill="#e21b2c" d="M6.6 10.8a15.1 15.1 0 0 0 6.6 6.6l2.2-2.2c.3-.3.7-.4 1-.2 1.1.4 2.3.6 3.6.6.6 0 1 .4 1 1V20c0 .6-.4 1-1 1A17 17 0 0 1 3 4c0-.6.4-1 1-1h3.5c.6 0 1 .4 1 1 0 1.3.2 2.5.6 3.6.1.3 0 .7-.2 1z"/></svg>
        1800 555 014
      </span>
      <span>
        <svg width="22" height="16" viewBox="0 0 22 16" aria-hidden="true"><rect x="0" y="0" width="22" height="16" fill="#e21b2c"/><polyline points="0,0 11,9 22,0" fill="none" stroke="#fff" stroke-width="1.5"/></svg>
        info@cellarloop.com.au
      </span>
    </div>
  </footer>
</div>
</body>
</html>
```